Amber Ridge Tobacco wraps

We need packaging designs for a tobacco leaf product that we are bringing to the market. We already have a logo that we would like added to the packaging. The packaging is for a zipper bag that will be sealed and place in a display box that will be placed on the counter. We like a design to compliment the logo. We will attach the logo here for ease of reference.

Target Market(s)

Smokers who use tobacco or cannabis

Industry/Entity Type

Smoking, tobacco, cannabis

Requirements
Must have
• Barcodes, warning label, space for socials
Should not have
• The package should not have a clear window

```html
<!DOCTYPE html>
<html lang="en">
<head>
<meta charset="utf-8">
<title>Amber Ridge Wrap &amp; Roll Pouch</title>
<link rel="stylesheet" href="https://fonts.googleapis.com/css2?family=Rye&family=Roboto+Slab:wght@700;800&family=Lobster&family=Archivo+Black&family=Archivo:wght@700;800&family=Libre+Baskerville:wght@700&display=swap">
<style>
  :root {
    --cream: #efeadb;
    --cream-light: #f4f0e4;
    --green: #1f5a36;
    --green-deep: #184a2b;
    --taupe: #9a807a;
    --taupe-light: #c9b8b0;
    --yellow: #e4e45c;
    --rasta-red: #b8262a;
    --rasta-gold: #d9c43a;
    --rasta-green: #2c7a35;
    --page: #ffffff;
  }
  * { margin: 0; padding: 0; box-sizing: border-box; }
  html, body { width: 886px; height: 1200px; overflow: hidden; background: var(--page); }
  .canvas { position: relative; width: 886px; height: 1200px; }

  .pouch {
    position: absolute; left: 208px; top: 25px; width: 470px; height: 1150px;
    background: var(--cream); border-radius: 18px 18px 6px 6px; overflow: hidden;
  }
  .frame {
    position: absolute; left: 38px; top: 82px; width: 394px; height: 904px;
    border: 1px solid var(--taupe-light);
  }
  .frame-inner {
    position: absolute; left: 46px; top: 90px; width: 378px; height: 888px;
    border: 1px solid var(--taupe-light); opacity: .7;
  }

  .tagline {
    position: absolute; left: 90px; top: 96px; width: 263px; height: 29px;
    background: var(--yellow); border-radius: 4px;
    font: 400 24px/29px "Lobster", cursive; color: var(--taupe);
    text-align: center; letter-spacing: 1px;
  }

  .brand-name {
    position: absolute; left: 0; width: 100%; text-align: center;
    font-family: "Rye", serif; color: var(--green); text-transform: uppercase;
  }
  .brand-name.line-one { top: 132px; font-size: 78px; line-height: 92px; }
  .brand-name.line-two { top: 236px; font-size: 80px; line-height: 100px; }

  .subtitle-arc { position: absolute; left: 0; top: 316px; width: 470px; height: 80px; }
  .subtitle-arc text { font-family: "Archivo Black", sans-serif; fill: var(--taupe); }

  .illustration {
    position: absolute; left: 99px; top: 430px; width: 250px; height: 338px;
    background:
      linear-gradient(180deg, rgba(0,0,0,0) 60%, var(--cream) 100%),
      linear-gradient(90deg, var(--rasta-green) 0%, var(--rasta-gold) 45%, var(--rasta-red) 75%);
    border-radius: 46% 46% 30% 30%;
    opacity: .9;
  }
  .ornament-left, .ornament-right {
    position: absolute; top: 400px; width: 70px; height: 330px;
    background: linear-gradient(180deg, rgba(154,128,122,.08), rgba(154,128,122,.16), rgba(154,128,122,.05));
    border-radius: 30px;
  }
  .ornament-left { left: 52px; }
  .ornament-right { right: 52px; }

  .seal {
    position: absolute; top: 707px; width: 60px; height: 60px; border-radius: 50%;
    border: 2px solid var(--taupe); background: var(--cream);
    display: flex; flex-direction: column; align-items: center; justify-content: center; text-align: center;
  }
  .seal.leaf-count { left: 70px; color: var(--green-deep); }
  .seal.leaf-count .count { font: 800 30px/26px "Roboto Slab", serif; }
  .seal.leaf-count .unit { font: 700 10px/12px "Archivo", sans-serif; color: var(--taupe); }
  .seal.note { left: 321px; font: 700 7.5px/8.5px "Libre Baskerville", serif; color: var(--green); padding: 6px; }

  .certified {
    position: absolute; left: 176px; top: 778px; width: 106px; height: 20px;
    border: 1px solid var(--taupe-light); background: var(--cream-light);
    font: 700 10px/18px "Archivo", sans-serif; color: var(--taupe); text-align: center; letter-spacing: .8px;
  }
  .claim-box {
    position: absolute; left: 80px; top: 797px; width: 294px; height: 153px;
    border: 1.5px solid var(--taupe-light);
  }
  .claim-percent {
    position: absolute; left: 42px; top: 14px; width: 40px; height: 102px;
    background: var(--yellow);
  }
  .claim-percent span {
    position: absolute; left: 50%; top: 50%; transform: translate(-50%,-50%) rotate(-90deg);
    font: 800 30px/1 "Roboto Slab", serif; color: var(--green); white-space: nowrap;
  }
  .claim-line {
    position: absolute; left: 96px; font-family: "Roboto Slab", serif; font-weight: 800; color: var(--green);
  }
  .claim-line.natural { top: 10px; font-size: 40px; line-height: 46px; }
  .claim-line.rolling { top: 56px; font-size: 40px; line-height: 46px; }
  .claim-line.leaf { top: 104px; left: 40px; font-size: 30px; line-height: 36px; }

  .descriptor {
    position: absolute; left: 0; top: 956px; width: 100%; text-align: center;
    font: 800 15px/24px "Archivo", sans-serif; color: var(--taupe); letter-spacing: .6px;
  }

  .warning-band {
    position: absolute; left: 0; top: 1014px; width: 100%; height: 136px;
    background: var(--green);
  }
  .warning-band span {
    position: absolute; left: 0; top: 60px; width: 100%; text-align: center;
    font: 800 17px/20px "Archivo", sans-serif; color: #fff; letter-spacing: 1.5px;
  }
</style>
</head>
<body>
<div class="canvas">
  <div class="pouch">
    <div class="frame"></div>
    <div class="frame-inner"></div>

    <div class="tagline">Finest Tobacco</div>

    <div class="brand-name line-one">Amber</div>
    <div class="brand-name line-two">Ridge</div>

    <svg class="subtitle-arc" viewBox="0 0 470 80" aria-label="Wrap and Roll Premium">
      <defs><path id="wrap-arc" d="M70 30 Q235 70 400 30"/></defs>
      <text font-size="30" letter-spacing="1"><textPath href="#wrap-arc" startOffset="50%" text-anchor="middle">WRAP &amp; ROLL</textPath></text>
      <text x="235" y="62" font-size="10" text-anchor="middle" letter-spacing="3">PREMIUM</text>
    </svg>

    <div class="ornament-left" role="img" aria-label="Engraved tobacco leaf ornament"></div>
    <div class="ornament-right" role="img" aria-label="Engraved tobacco leaf ornament"></div>
    <div class="illustration" role="img" aria-label="Illustrated character portrait in red, gold and green"></div>

    <div class="seal leaf-count"><span class="unit">LEAF</span><span class="count">1</span></div>
    <div class="seal note">Lorem ipsum dolor sit amet, consec-</div>

    <div class="certified">CERTIFIED</div>
    <div class="claim-box">
      <div class="claim-percent"><span>100%</span></div>
      <div class="claim-line natural">Natural</div>
      <div class="claim-line rolling">Rolling</div>
      <div class="claim-line leaf">Grabba Leaf</div>
    </div>

    <div class="descriptor">LOREM IPSUM DOLOR SIT<br>AMET, CONSECTETUER</div>

    <div class="warning-band"><span>WARNING</span></div>
  </div>
</div>
</body>
</html>
```